Briarloft Business Card 2

Hi you submited a design for us on a defferent project. Your design number was 4076083.

I would like to use this design but need to make some changes.

Please remove the name and position.
Remove mobile number.
and Change email to info@briarloft.com.au

Industry/Entity Type

Business

```html
<!DOCTYPE html>
<html lang="en">
<head>
<meta charset="utf-8">
<title>Briarloft Business Card</title>
<link href="https://fonts.googleapis.com/css2?family=Montserrat:wght@600;700&family=Lato:wght@400&display=swap" rel="stylesheet">
<style>
  :root {
    --backdrop: #e9e6e1;
    --card-dark: #2b2b2b;
    --card-light: #ffffff;
    --ink: #232323;
    --lime: #a6d32f;
    --charcoal: #2f2f2f;
  }
  * { box-sizing: border-box; margin: 0; padding: 0; }
  html, body { width: 1200px; height: 1000px; overflow: hidden; }
  body { background: var(--backdrop); position: relative; font-family: "Lato", sans-serif; }

  .card-back {
    position: absolute; left: 80px; top: 120px; width: 840px; height: 480px;
    background: var(--card-dark); box-shadow: 0 10px 30px rgba(0,0,0,.25);
  }
  .card-back__texture {
    position: absolute; inset: 0;
    background: linear-gradient(135deg, #303030, #262626);
  }
  .card-back__name {
    position: absolute; left: 500px; top: 150px;
    font-family: "Montserrat", sans-serif; font-weight: 700; font-size: 34px;
    color: var(--card-light); letter-spacing: 1px;
  }

  .card-front {
    position: absolute; left: 175px; top: 420px; width: 815px; height: 460px;
    background: var(--card-light); box-shadow: 0 12px 34px rgba(0,0,0,.3);
    overflow: hidden;
  }
  .brand { position: absolute; left: 45px; top: 62px; }
  .brand__name {
    display: flex; align-items: center; gap: 16px;
    font-family: "Montserrat", sans-serif; font-weight: 700; font-size: 56px;
    line-height: 1; color: var(--lime); letter-spacing: 1px;
  }
  .brand__square { width: 44px; height: 44px; background: var(--charcoal); }
  .brand__tagline {
    margin-top: 14px; margin-left: 62px;
    font-family: "Montserrat", sans-serif; font-weight: 600; font-size: 25px;
    color: var(--ink); letter-spacing: 2px;
  }
  .corner-accent {
    position: absolute; right: 0; top: 140px; width: 120px; height: 190px;
    background: linear-gradient(135deg, var(--charcoal) 0 45%, var(--lime) 45% 100%);
  }
  .contacts { position: absolute; left: 45px; top: 285px; list-style: none; }
  .contacts li {
    display: flex; align-items: center; gap: 12px;
    font-size: 21px; color: var(--ink); height: 32px;
  }
  .contacts svg { width: 20px; height: 20px; fill: var(--lime); flex: none; }
  .band { position: absolute; bottom: 0; height: 12px; }
  .band--dark { left: 0; width: 520px; background: var(--charcoal); clip-path: polygon(0 0,100% 0,97% 100%,0 100%); }
  .band--lime { left: 510px; right: 0; background: var(--lime); clip-path: polygon(3% 0,100% 0,100% 100%,0 100%); }
</style>
</head>
<body>
  <section class="card-back">
    <div class="card-back__texture" role="img" aria-label="Dark woven pattern background"></div>
    <div class="card-back__name">BRIARLOFT</div>
  </section>

  <section class="card-front">
    <div class="brand">
      <div class="brand__name"><span class="brand__square"></span>BRIARLOFT</div>
      <div class="brand__tagline">PLANTATION SHUTTERS</div>
    </div>

    <div class="corner-accent" role="img" aria-label="Brand accent stripes"></div>

    <ul class="contacts">
      <li><svg viewBox="0 0 24 24"><path d="M6.6 10.8a15 15 0 0 0 6.6 6.6l2.2-2.2c.3-.3.7-.4 1-.2 1.1.4 2.3.6 3.6.6.6 0 1 .4 1 1V20c0 .6-.4 1-1 1A17 17 0 0 1 3 4c0-.6.4-1 1-1h3.5c.6 0 1 .4 1 1 0 1.3.2 2.5.6 3.6.1.3 0 .7-.2 1z"/></svg>1300 555 014</li>
      <li><svg viewBox="0 0 24 24"><path d="M2 5h20v14H2z M2 5l10 7 10-7" /></svg>info@briarloft.com.au</li>
      <li><svg viewBox="0 0 24 24"><path d="M12 2a7 7 0 0 0-7 7c0 5 7 13 7 13s7-8 7-13a7 7 0 0 0-7-7zm0 9.5A2.5 2.5 0 1 1 12 6.5a2.5 2.5 0 0 1 0 5z"/></svg>24 Harlow Lane, Kingsbury, VIC 3083, Australia</li>
      <li><svg viewBox="0 0 24 24"><circle cx="12" cy="12" r="10"/></svg>www.briarloft.com.au</li>
    </ul>

    <div class="band band--dark"></div>
    <div class="band band--lime"></div>
  </section>
</body>
</html>
```